Conference Oversize Name Badge

Design an oversized name badge that would be worn by conference attendees using a lanyard.

Things to include on the name badge
- attendee's headshot (photo)
- attendee's first name and last name
- attendee's company name
- conference organizer company name
- conference organizer logo (attached)
- barcode
- attendee type color theme. For example: sponsor would have a red color theme, exhibitor would have blue color theme. Same badges but with different color themes.

Get creative!

Please let me know if you have any questions.

Industry/Entity Type

Event Planning

Requirements
Must have
• Whats important:
• 1. Attendee name and company name needs to be big and prominent and easily readable.
• 2. Incorporate attached conference organizer logo
• 3. Be creative
Should not have
• Please do not submit boring rectangle name badges.

```html
<!DOCTYPE html>
<html lang="en">
<head>
<meta charset="utf-8">
<title>Conference Badge – Sponsor</title>
<link href="https://fonts.googleapis.com/css2?family=Fredoka:wght@600&family=Josefin+Sans:wght@300&display=swap" rel="stylesheet">
<style>
  :root {
    --card: #f8f0f0;
    --ink-deep: #4e1c1e;
    --ink-mid: #6b2a2c;
    --ink-soft: #8a6a6b;
    --sponsor: #3a1010;
    --sponsor-shadow-a: #6f6a45;
    --sponsor-shadow-b: #e0394a;
    --brand-teal: #3f8aa3;
    --org-ink: #2a2a2a;
  }
  html, body {
    margin: 0;
    width: 900px;
    height: 1200px;
    overflow: hidden;
    background: var(--card);
  }
  .badge {
    position: relative;
    width: 900px;
    height: 1200px;
    overflow: hidden;
    background: var(--card);
  }
  .band {
    position: absolute;
    left: 0;
    width: 900px;
  }
  .band--top { top: 0; height: 170px; }
  .band--bottom { top: 980px; height: 220px; }
  .band svg { display: block; }

  .backdrop-portrait {
    position: absolute;
    left: 560px; top: 130px;
    width: 340px; height: 870px;
    background: linear-gradient(90deg, rgba(248,240,240,0) 0%, rgba(214,196,192,.55) 35%, rgba(222,205,198,.6) 100%);
  }

  .organizer {
    position: absolute;
    top: 190px; left: 0;
    width: 900px;
    display: flex;
    justify-content: center;
    align-items: center;
    gap: 18px;
  }
  .organizer__dot {
    width: 70px; height: 70px;
    border-radius: 50%;
    background: var(--brand-teal);
  }
  .organizer__name {
    font: 300 33px "Josefin Sans", sans-serif;
    color: var(--org-ink);
  }

  .headshot {
    position: absolute;
    left: 317px; top: 289px;
    width: 274px; height: 338px;
    border: 3px solid #111;
    background: linear-gradient(180deg, #d8d4d6 0%, #c9a58f 45%, #b98d76 75%, #dfe4ee 100%);
  }

  .attendee {
    position: absolute;
    left: 0; width: 900px;
    text-align: center;
    font-family: "Fredoka", sans-serif;
    font-weight: 600;
    margin: 0;
  }
  .attendee__first { top: 628px; font-size: 218px; line-height: 1; color: var(--ink-deep); letter-spacing: -2px; }
  .attendee__last { top: 836px; font-size: 92px; line-height: 1; color: var(--ink-mid); }
  .attendee__company { top: 940px; font-size: 43px; line-height: 1; color: var(--ink-soft); }

  .attendee-type {
    position: absolute;
    left: 0; top: 1020px;
    width: 900px;
    text-align: center;
    font: 600 212px/1 "Fredoka", sans-serif;
    color: var(--sponsor);
    letter-spacing: 2px;
    text-shadow: -14px -8px 0 var(--sponsor-shadow-a), 10px 6px 0 var(--sponsor-shadow-b);
  }
</style>
</head>
<body>
<main class="badge">
  <div class="band band--top" role="img" aria-label="Warm red header with multilingual greeting word pattern">
    <svg width="900" height="170" viewBox="0 0 900 170">
      <defs>
        <linearGradient id="topBand" x1="0" y1="0" x2="1" y2="1">
          <stop offset="0" stop-color="#c3665a"/>
          <stop offset=".5" stop-color="#d47f64"/>
          <stop offset="1" stop-color="#c25c55"/>
        </linearGradient>
      </defs>
      <polygon fill="url(#topBand)" points="0,0 900,0 900,165 825,130 750,165 675,130 600,165 525,130 450,165 375,130 300,165 225,130 150,165 75,130 0,165"/>
    </svg>
  </div>

  <div class="backdrop-portrait" role="img" aria-label="Faded enlarged attendee portrait background"></div>

  <div class="organizer">
    <span class="organizer__dot"></span>
    <span class="organizer__name">Summit Gather LLC</span>
  </div>

  <div class="headshot" role="img" aria-label="Attendee headshot photo"></div>

  <h1 class="attendee attendee__first">Lucile</h1>
  <h2 class="attendee attendee__last">Hartwell</h2>
  <p class="attendee attendee__company">Harlow &amp; Sons Life Assurance</p>

  <div class="band band--bottom" role="img" aria-label="Warm red geometric pattern footer">
    <svg width="900" height="220" viewBox="0 0 900 220">
      <defs>
        <linearGradient id="bottomBand" x1="0" y1="0" x2="1" y2="1">
          <stop offset="0" stop-color="#c86a58"/>
          <stop offset=".5" stop-color="#d9856a"/>
          <stop offset="1" stop-color="#d04a4f"/>
        </linearGradient>
      </defs>
      <polygon fill="url(#bottomBand)" points="0,40 75,5 150,40 225,5 300,40 375,5 450,40 525,5 600,40 675,5 750,40 825,5 900,40 900,220 0,220"/>
    </svg>
  </div>

  <div class="attendee-type">SPONSER</div>
</main>
</body>
</html>
```